Health Coaching Brochure for Healthcare Practioners

I am looking to have a tri-fold brochure created marketed towards healthcare practitioners (doctors, nurses, surgeons, etc), to get them to purchase 1-on-1 health coaching from me.
I've provided the text/content (in pdf & pages), my logo, a picture of me, and two color palettes, but please also include lots of white space. I would like to design to be very clean, modern & crisp. Also include additional photos, of doctors, etc taking care of themselves & feeling happy (maybe eating healthy, maybe exercising, feeling good & happy!)
Please also see http://tallbirchwellness.com and http://instagram.com/tallbirchwellness for a feel of my brand.
Thank you!
Target Market(s)
Healthcare Practioners (mainly based in Los Angeles, for now)
Industry/Entity Type
Healthcare
Look and feel
Each slider illustrates characteristics of the customer's brand and the style your logo design should communicate.

```html
<!DOCTYPE html>
<html lang="en">
<head>
<meta charset="utf-8">
<title>Tall Birch Wellness – Tri-fold Brochure</title>
<link href="https://fonts.googleapis.com/css2?family=Hind:wght@400;500;600;700&family=Lora:ital@1&display=swap" rel="stylesheet">
<style>
:root{
  --blue:#3a78b5;
  --blue-dark:#2b64a3;
  --cyan:#2ec4f1;
  --white:#ffffff;
  --ink:#4a4f55;
  --page:#d5d6d8;
  --photo-food:#c9a25a;
  --photo-sky:#b9d4ea;
  --photo-skin:#c9a591;
  --photo-green:#6fae3e;
  --photo-clinic:#dfe6ec;
}
*{margin:0;padding:0;box-sizing:border-box}
html,body{width:817px;height:1200px;overflow:hidden}
body{background:var(--page);font-family:"Hind",sans-serif;color:var(--ink);position:relative}
.spread{position:absolute;left:80px;width:648px;height:504px;display:flex;background:var(--white)}
.spread--outside{top:67px}
.spread--inside{top:622px}
.panel{position:relative;height:100%;overflow:hidden}
.panel--blue{background:var(--blue);color:var(--white)}
.panel--white{background:var(--white)}
.w212{width:212px}.w216{width:216px}.w220{width:220px}
.abs{position:absolute}
.heading{font-weight:700;font-size:9px;line-height:1.25;text-transform:uppercase}
.body-text{font-size:8.6px;line-height:1.22;text-align:justify}
.bullets{list-style:none;font-size:8.6px;line-height:13.8px}
.bullets li{position:relative;padding-left:10px}
.bullets li::before{content:"";position:absolute;left:0;top:4px;width:6px;height:6px;border-radius:50%;background:var(--white)}
.ticks{list-style:none;font-size:9.6px;line-height:13.4px;color:#4d5560}
.ticks li{position:relative;padding-left:16px}
.ticks li::before{content:"";position:absolute;left:2px;top:3px;width:6px;height:6px;border:1px solid var(--blue);border-radius:50%}
.questions{list-style:none;font-size:8.3px;line-height:10.5px;color:#5b6168}
.questions li{position:relative;padding-left:12px;margin-bottom:10.5px}
.questions li::before{content:"";position:absolute;left:0;top:2px;width:6px;height:6px;border:1px solid var(--blue);border-radius:50%}
.wordmark{font-weight:600;font-size:17px;letter-spacing:.2px;text-align:center;width:100%}
.phone-btn{background:var(--cyan);color:var(--white);border-radius:6px;height:22px;font-weight:600;font-size:13px;display:flex;align-items:center;justify-content:center;gap:4px}
.phone-btn svg{width:12px;height:12px}
.center{text-align:center}
.title-spaced{letter-spacing:1.6px;font-weight:500;font-size:14.5px;line-height:15px;text-align:center}
.quote{font-size:8.6px;line-height:10.6px}
.quote-mark{position:absolute;left:-20px;top:-3px;font-size:18px;font-weight:700;color:#b9cde6}
</style>
</head>
<body>

<!-- OUTSIDE SPREAD -->
<section class="spread spread--outside">
  <div class="panel panel--blue w212">
    <h2 class="heading abs" style="left:13px;top:52px">About Tall Birch Wellness</h2>
    <p class="body-text abs" style="left:13px;top:73px;width:186px">Maya Lindqvist is holistic health coach, personal trainer, and fitness nutritionist who empowers healthcare practitioners who are exhausted and overwhelmed to find uncomplicated ways to minimize their stress and to make themselves and their health a priority.</p>
    <h3 class="heading abs" style="left:13px;top:175px">Services include:</h3>
    <ul class="bullets abs" style="left:13px;top:191px">
      <li>1-on-1 Virtuel Health Coaching</li>
      <li>1-on-1 Personal Training</li>
      <li>Virtuel Group Coaching</li>
      <li>Custom Workouth Program and/or Meal Plan</li>
      <li>Grocery Store Tour</li>
      <li>Pantry Clean Out</li>
    </ul>
    <svg class="abs" style="left:0;top:310px" width="212" height="194" viewBox="0 0 212 194" role="img" aria-label="Portrait photo of the coach smiling">
      <path d="M0 14 Q90 -6 212 24 L212 194 L0 194Z" fill="var(--cyan)"/>
      <path d="M0 24 Q90 6 212 34 L212 194 L0 194Z" fill="var(--photo-skin)"/>
    </svg>
  </div>

  <div class="panel panel--white w216">
    <svg class="abs" style="left:0;top:0" width="216" height="170" viewBox="0 0 216 170" role="img" aria-label="Photo of a bowl of fresh vegetables">
      <path d="M6 0 L208 0 Q214 120 130 160 Q50 180 10 100Z" fill="var(--photo-food)"/>
    </svg>
    <div class="abs" style="left:20px;top:75px;width:105px;height:105px;border-radius:50%;background:var(--cyan)"></div>
    <p class="abs" style="left:23px;top:102px;width:100px;font-family:'Lora',serif;font-style:italic;font-size:7.6px;line-height:10.6px;color:var(--white)">Together we can reclaim your health and create a life more joyful than you ever imagined!</p>
    <p class="wordmark abs" style="top:212px;color:#5a5f66">Tall Birch Wellness</p>
    <p class="abs center heading" style="top:253px;width:100%;color:var(--blue);font-size:9.4px">Westside location or<br>at-home workouts</p>
    <p class="abs center" style="top:292px;width:100%;font-size:8.6px;font-weight:600;color:#5b6168">call for a free 15 minute consultation</p>
    <div class="phone-btn abs" style="left:33px;top:310px;width:150px">
      <svg viewBox="0 0 24 24"><circle cx="12" cy="12" r="10.5" fill="none" stroke="#fff" stroke-width="2"/><path d="M8.5 7c.6 3.7 3.5 7.4 8 8.5l.8-1.8-2.2-1.3-1 1c-1.4-.7-2.6-1.9-3.3-3.3l1-1-1.3-2.2z" fill="#fff"/></svg>
      555.201.4476
    </div>
    <p class="abs center" style="top:343px;width:100%;font-size:10px;line-height:12.5px;color:#5b6168">1-ON-1 PERSONAL TRAINING,<br>LOS ANGELES, CA</p>
    <svg class="abs" style="left:0;top:396px" width="216" height="108" viewBox="0 0 216 108" role="img" aria-label="Photo of a green smoothie in a glass">
      <path d="M56 108 A80 80 0 0 1 190 40" fill="none" stroke="var(--blue)" stroke-width="8"/>
      <circle cx="132" cy="80" r="66" fill="var(--photo-green)"/>
    </svg>
  </div>

  <div class="panel panel--blue w220">
    <svg class="abs" style="left:0;top:0" width="220" height="300" viewBox="0 0 220 300" role="img" aria-label="Photo of a woman in a white dress with arms open in a sunny field">
      <path d="M0 0 H220 V290 Q150 230 80 250 Q30 262 0 218Z" fill="var(--photo-sky)"/>
      <path d="M0 210 Q40 258 90 244 Q160 222 220 282" fill="none" stroke="var(--cyan)" stroke-width="5"/>
    </svg>
    <p class="wordmark abs" style="top:318px;color:var(--white)">Tall Birch Wellness</p>
    <svg class="abs" style="left:0;top:370px" width="220" height="134" viewBox="0 0 220 134">
      <path d="M0 14 Q110 -12 220 40 L220 134 L0 134Z" fill="var(--cyan)"/>
      <path d="M0 22 Q110 -2 220 52 L220 134 L0 134Z" fill="var(--white)"/>
    </svg>
    <h2 class="title-spaced abs" style="left:0;width:220px;top:401px;color:var(--blue)">CHANGE<br>THE WAY YOU LIVE</h2>
    <ul class="ticks abs" style="left:27px;top:440px">
      <li>GET IN SHAPE</li>
      <li>LOSE WEIGHT</li>
      <li>TONE UP</li>
      <li>LOOK &amp; FEEL BETTER THAN EVER</li>
    </ul>
  </div>
</section>

<!-- INSIDE SPREAD -->
<section class="spread spread--inside">
  <div class="panel panel--blue w216">
    <svg class="abs" style="left:0;top:0" width="216" height="196" viewBox="0 0 216 196" role="img" aria-label="Photo of two smiling doctors using a scale">
      <path d="M0 0 H216 V160 Q130 196 60 186 Q25 180 0 172Z" fill="var(--photo-clinic)"/>
      <path d="M0 178 Q60 194 120 184 Q180 172 216 156" fill="none" stroke="var(--cyan)" stroke-width="5"/>
    </svg>
    <h2 class="heading abs" style="left:13px;top:213px">Get the most out of<br>your workout by working out<br>with a personal trainer</h2>
    <ul class="bullets abs" style="left:13px;top:256px">
      <li>Customized workout program,</li>
      <li>from beginnier to advanced</li>
      <li>Provide motivation, support, and accountability</li>
      <li>Integrative Nutrition &amp; Health Coaching</li>
      <li>+24-hour access to trainer</li>
    </ul>
    <h2 class="heading abs" style="left:13px;top:340px">Achieve your fitness goals<br>and have fun doing it</h2>
    <ul class="bullets abs" style="left:13px;top:369px">
      <li>Fat Loss</li>
      <li>Weight Training</li>
      <li>Cardiovascular Training</li>
      <li>Muscular Development &amp; Toning</li>
      <li>Sports Performance Training</li>
      <li>Body Composition Analysis</li>
      <li>Specialized Diet Plans</li>
      <li>Nutrition &amp; Supplementation Counseling</li>
      <li>Wedding Preparation</li>
    </ul>
  </div>

  <div class="panel panel--white w212">
    <div class="abs" style="left:18px;top:-40px;width:176px;height:120px;border-radius:0 0 88px 88px / 0 0 70px 70px;background:var(--blue)"></div>
    <p class="abs center" style="left:18px;width:176px;top:20px;font-size:8.6px;line-height:13.5px;color:var(--white)"><b>FUNCTION MOVEMENTS!</b><br>based on how your body was<br>designed to move</p>
    <div class="abs" style="left:75px;top:60px;width:100px;height:100px;border-radius:50%;background:var(--cyan)"></div>
    <p class="abs center" style="left:75px;width:100px;top:90px;font-size:9.4px;line-height:13px;font-weight:600;color:var(--white)">It's time to take<br>care of YOU.<br>You deserve it!</p>
    <p class="abs center" style="left:4px;width:204px;top:174px;font-size:9.6px;line-height:12px;font-weight:600;color:var(--blue)">Are you overwhelmed and exhausted and feel like there's no time left for YOU?</p>
    <ul class="questions abs" style="left:12px;top:210px;width:196px">
      <li>Do you put everyone and everything else before your own health?</li>
      <li>Are you struggling with how to fit in exercise after working 12-15 hours shifts?</li>
      <li>Do you know exactly what you should do take care of yourself, but it's just not happening?</li>
      <li>Have you gained weight due to stress-eating, and ready to take it off?</li>
      <li>Are you ready to feel energetic and sexy and to fully love yourself again?</li>
    </ul>
    <p class="abs center" style="left:0;width:212px;top:407px;font-size:9px;line-height:12.5px;font-weight:700;color:var(--blue)">READY TO MAKE THE COMMITMENT?<br>schedule your 15 minute consultation today!</p>
    <div class="phone-btn abs" style="left:27px;top:441px;width:150px">
      <svg viewBox="0 0 24 24"><circle cx="12" cy="12" r="10.5" fill="none" stroke="#fff" stroke-width="2"/><path d="M8.5 7c.6 3.7 3.5 7.4 8 8.5l.8-1.8-2.2-1.3-1 1c-1.4-.7-2.6-1.9-3.3-3.3l1-1-1.3-2.2z" fill="#fff"/></svg>
      555.201.4476
    </div>
    <p class="body-text abs" style="left:7px;top:474px;width:198px;font-size:8px;line-height:10px;color:#6a7077">As healthcare practitioners, it's easy to lose sight of your own wants and needs, when you're so busy taking care of everyone else.</p>
  </div>

  <div class="panel panel--blue w220">
    <h2 class="title-spaced abs" style="left:0;width:220px;top:28px;color:var(--white)">CHANGE<br>THE WAY YOU LIVE</h2>
    <p class="body-text abs" style="left:12px;top:68px;width:198px;font-size:7.6px;line-height:9.8px">Helping others is my passion. Seeing the change in someone throughout their fitness journey is incredible. Not just physically, but also emotionally. They have become more confident, more optimistic, healthier and stronger in all aspects of their life.</p>
    <p class="body-text abs" style="left:12px;top:124px;width:198px;font-size:7.6px;line-height:9.8px">Working with all different skill sets and fitness levels I am always working for my clients. Doing everything I can to teach them how to live a healthier life.</p>
    <div class="quote abs" style="left:32px;top:182px;width:178px">
      <span class="quote-mark">“</span>
      <p>I am so happy with the results!</p>
      <p style="margin-top:10px;text-align:justify">The fogginess is gone (as are my sugar cravings). I've found new ways to add healthy foods into my diet and (bonus) I lost five pounds the first week!</p>
      <p style="margin-top:12px">Dana Ruiz</p>
    </div>
    <div class="quote abs" style="left:32px;top:282px;width:178px">
      <span class="quote-mark">“</span>
      <p style="text-align:justify">She's helped me transform myself from an overweight junk food eater to a much fitter and healthier person.</p>
      <p style="margin-top:10px">I highly recommend Maya to anyone and everyone.</p>
      <p style="margin-top:10px">Kelly Moss</p>
    </div>
    <svg class="abs" style="left:0;top:382px" width="220" height="122" viewBox="0 0 220 122" role="img" aria-label="Photo of a doctor beside fresh fruit and a tape measure">
      <path d="M0 30 Q90 -4 220 8 L220 122 L0 122Z" fill="var(--cyan)"/>
      <path d="M0 38 Q90 4 220 16 L220 122 L0 122Z" fill="var(--photo-clinic)"/>
    </svg>
  </div>
</section>

</body>
</html>
```